Indy Film Production Company/Studio

We need a business card designed from an existing logo. We are a digital studio/production company that caters to creating genre entertainment, like Action, Horror, and martial arts. The card along with the logo will be used to Brand the company from letter heads to banners. The design will also be used for postcards and Brochures. It should be professional and masculine.
Updates

Thank you to all the designers who have participated. I'm narrowing down who it will be. Thank you again.

Target Market(s)

Investors, Networks, Producers, and actors

Industry/Entity Type

Film Production

Contact Information for Business Card

Benedict Harlowe
Producer/Writer/Director
www.pelvarmotionworks.com

Requirements
Must have
• Website address, Facebook icon and Twitter icon possibly in the back of the card.
Nice to have
• Logline of Company: Follow The Action.

```html
<!DOCTYPE html>
<html lang="en">
<head>
<meta charset="utf-8">
<title>Pelvar Motion Works – Business Card</title>
<link href="https://fonts.googleapis.com/css2?family=Montserrat:ital,wght@1,800&family=Roboto:wght@400;900&display=swap" rel="stylesheet">
<style>
  :root {
    --backdrop: #a9a7a7;
    --brand-red: #cd2f29;
    --card-white: #f4f4f3;
    --ink: #1c1c1c;
    --ink-soft: #2a2a2a;
    --divider: #dcdcdc;
  }
  html, body {
    margin: 0;
    padding: 0;
    width: 1200px;
    height: 1200px;
    overflow: hidden;
    background: var(--backdrop);
  }
  .canvas {
    position: relative;
    width: 1200px;
    height: 1200px;
  }
  .card {
    position: absolute;
    box-sizing: border-box;
  }
  .card--front {
    left: 238px;
    top: 118px;
    width: 722px;
    height: 419px;
    background: var(--brand-red);
    display: flex;
    align-items: center;
    justify-content: center;
  }
  .card--back {
    left: 230px;
    top: 643px;
    width: 738px;
    height: 419px;
    background: var(--card-white);
  }
  .wordmark {
    margin: 0;
    font-family: "Roboto", Arial, sans-serif;
    font-weight: 900;
    text-transform: uppercase;
    text-align: center;
    line-height: 0.95;
    letter-spacing: 1px;
  }
  .wordmark--front {
    color: #ffffff;
    font-size: 54px;
  }
  .wordmark--back {
    position: absolute;
    left: 54px;
    top: 150px;
    width: 250px;
    color: var(--brand-red);
    font-size: 38px;
  }
  .divider {
    position: absolute;
    left: 338px;
    top: 88px;
    width: 1px;
    height: 262px;
    background: var(--divider);
  }
  .contact {
    position: absolute;
    left: 375px;
    top: 110px;
    width: 340px;
    font-family: "Roboto", Arial, sans-serif;
    color: var(--ink-soft);
  }
  .contact__name {
    margin: 0;
    font-family: "Montserrat", Arial, sans-serif;
    font-style: italic;
    font-weight: 800;
    font-size: 26px;
    color: var(--ink);
    line-height: 1.2;
  }
  .contact__role {
    margin: 6px 0 0;
    font-size: 16px;
    color: var(--brand-red);
  }
  .contact__list {
    list-style: none;
    margin: 28px 0 0;
    padding: 0;
    font-size: 18px;
    line-height: 28px;
  }
  .contact__item {
    display: flex;
    align-items: center;
    gap: 16px;
  }
  .contact__icon {
    width: 18px;
    height: 14px;
    fill: var(--brand-red);
    flex: none;
  }
  .contact__address {
    margin: 0;
    font-size: 18px;
    line-height: 28px;
    font-style: normal;
  }
  .social {
    display: flex;
    gap: 10px;
    margin-top: 12px;
  }
  .social__badge {
    width: 22px;
    height: 22px;
    border-radius: 50%;
    background: var(--brand-red);
  }
</style>
</head>
<body>
<main class="canvas">
  <section class="card card--front" aria-label="Card front">
    <h1 class="wordmark wordmark--front">Pelvar<br>Motion Works</h1>
  </section>

  <section class="card card--back" aria-label="Card back">
    <p class="wordmark wordmark--back">Pelvar<br>Motion Works</p>
    <div class="divider"></div>
    <div class="contact">
      <h2 class="contact__name">Benedict Harlowe</h2>
      <p class="contact__role">Producer / Writer / Director</p>
      <ul class="contact__list">
        <li class="contact__item">
          <svg class="contact__icon" viewBox="0 0 18 14" aria-hidden="true">
            <path d="M1 4 C1 1 17 1 17 4 L17 5 L13 5 L13 3.5 C11 3 7 3 5 3.5 L5 5 L1 5 Z"/>
            <path d="M4 7 L6 5 L12 5 L14 7 L15 13 L3 13 Z"/>
          </svg>
          <span>+00 111 222 3333</span>
        </li>
        <li class="contact__item">
          <svg class="contact__icon" viewBox="0 0 18 14" aria-hidden="true">
            <circle cx="9" cy="7" r="6" fill="none" stroke="currentColor" stroke-width="1.6" style="color:var(--brand-red)"/>
            <path d="M3 7 H15 M9 1 C6 4 6 10 9 13 C12 10 12 4 9 1" fill="none" stroke="currentColor" stroke-width="1.2" style="color:var(--brand-red)"/>
          </svg>
          <span>www.pelvarmotionworks.com</span>
        </li>
      </ul>
      <address class="contact__address">Your Long Commercial or<br>business address in 2 line</address>
      <div class="social">
        <span class="social__badge" role="img" aria-label="Social profile"></span>
        <span class="social__badge" role="img" aria-label="Social profile"></span>
      </div>
    </div>
  </section>
</main>
</body>
</html>
```